PELDRAX Business Cards

We require a business card for our company that provides IT consulting services. We already have a logo that needs to be used on the card. We want a clean professional looking design that incorporates our colours. Our main focus is providing managed services to business, which involves us looking after all of their IT requirements including managing servers/networks, projects, and procurement.

Industry/Entity Type

Information Technology

Requirements
Must have
• our logo, contact information, name, title, phone numbers

```html
<!DOCTYPE html>
<html lang="en">
<head>
<meta charset="UTF-8">
<title>PELDRAX Business Cards</title>
<link href="https://fonts.googleapis.com/css2?family=Oswald:wght@500&family=Work+Sans:wght@400;600&display=swap" rel="stylesheet">
<style>
  :root {
    --brand-blue: #1596d1;
    --ink: #3a3d42;
    --paper: #ffffff;
    --backdrop: #1d2024;
  }
  * { margin: 0; padding: 0; box-sizing: border-box; }
  html, body { width: 1200px; height: 738px; overflow: hidden; background: var(--backdrop); }
  .sheet {
    position: relative; width: 1200px; height: 738px;
    display: flex; align-items: center; justify-content: center; gap: 40px;
  }
  .card {
    width: 520px; height: 297px; position: relative;
    box-shadow: 0 10px 30px rgba(0,0,0,.45);
  }
  .card-front {
    background: var(--brand-blue);
    display: flex; align-items: center; justify-content: center;
  }
  .brand { display: flex; align-items: center; gap: 16px; }
  .brand-dot { width: 44px; height: 44px; border-radius: 50%; background: var(--paper); }
  .brand-name {
    font-family: "Work Sans", sans-serif; font-weight: 600;
    font-size: 46px; letter-spacing: 4px; color: var(--paper);
  }
  .card-back { background: var(--paper); }
  .identity-row {
    position: absolute; top: 108px; left: 0; right: 0;
    display: flex; align-items: center; justify-content: center; gap: 18px;
  }
  .person { text-align: right; }
  .person-name {
    font-family: "Oswald", sans-serif; font-weight: 500;
    font-size: 32px; line-height: 1; letter-spacing: 1px;
    color: var(--brand-blue); text-transform: uppercase;
  }
  .person-title {
    font-family: "Work Sans", sans-serif; font-size: 13px;
    color: var(--ink); margin-top: 2px;
  }
  .divider { width: 2px; height: 46px; background: var(--brand-blue); }
  .contacts { list-style: none; font-family: "Work Sans", sans-serif; font-size: 13px; color: var(--ink); }
  .contacts li { display: flex; align-items: center; gap: 7px; line-height: 17px; }
  .contacts svg { width: 9px; height: 9px; fill: var(--brand-blue); flex: none; }
  .accent { color: var(--brand-blue); }
  .address {
    position: absolute; bottom: 42px; left: 0; right: 0; text-align: center;
    font-family: "Work Sans", sans-serif; font-size: 14px; letter-spacing: .5px; color: var(--ink);
  }
</style>
</head>
<body>
<main class="sheet">
  <section class="card card-front">
    <div class="brand">
      <span class="brand-dot"></span>
      <span class="brand-name">PELDRAX</span>
    </div>
  </section>

  <section class="card card-back">
    <div class="identity-row">
      <div class="person">
        <div class="person-name">Dorian Vale</div>
        <div class="person-title">Director</div>
      </div>
      <span class="divider"></span>
      <ul class="contacts">
        <li>
          <svg viewBox="0 0 10 10"><path d="M2 0.5 L3.6 2.6 L2.8 3.6 Q4 6 6.4 7.2 L7.4 6.4 L9.5 8 L8.4 9.5 Q1 8.5 0.5 1.6 Z"/></svg>
          555-310-2846
        </li>
        <li>
          <svg viewBox="0 0 10 10"><path d="M0 2 H10 V8.5 H0 Z M1 3 V7.5 H9 V3 L5 5.8 Z" fill-rule="evenodd"/></svg>
          info@peldrax.com
        </li>
        <li>
          <svg viewBox="0 0 10 10"><circle cx="5" cy="5" r="4.5"/></svg>
          www.<span class="accent">peldrax</span>.com
        </li>
      </ul>
    </div>
    <p class="address">48 Harbor Road Box 902, Lindenfield, AB</p>
  </section>
</main>
</body>
</html>
```